Selvin: A Friday night in the Prophetic Flyer

We are holding 2 Friday night events, one on 10/25/19 and the other on 11/29/19.
The time frame is 6:30pm-9:00pm. These services will be a time of prayer/healing for the sick and will be prophetic as well. (There will be prophets prophesying over people)

The event is called: Selvin: A Friday night in the Prophetic
The flyer should also include the phrase/excerpt: "And they prophesied also".

Keywords/Phrases: Prophetic, Healing, Climbing in the Spirit, Higher level of Anointing...

Target Market(s)

those looking for healing, seeking a word from God

Colors

Designer to choose colors to be used in the design.

Requirements
Must have
• The event is called: Selvin: A Friday night in the Prophetic
• The flyer should also include the phrase/excerpt: "And they prophesied also".
• It must include the Tovik logo attached, either is fine, we have attached two different versions.
• It must have the dates, location, time
• Dates: October 25, 2019 and November 29, 2019
• Location: Hollard Community Center
• (Downtown Portland) 482 Wendle Street
• Portland, ME 04102
• Time: 6:30pm-9:00pm
• Contact Info: Tel. 207-555-3841
• email: contact@brimfield-hall.org
• web: www.tovik.org
Nice to have
• creativity in color scheme, the meaning of the word Selvin conveyed in a classy artistic way/design.
Should not have
• Crosses, pictures of churches

```html
<!DOCTYPE html>
<html lang="en">
<head>
<meta charset="utf-8">
<title>Selvin: A Friday Night in the Prophetic</title>
<link href="https://fonts.googleapis.com/css2?family=Montserrat:ital,wght@0,400;0,500;0,700;0,800;0,900;1,500&family=Oswald:wght@500;600&display=swap" rel="stylesheet">
<style>
  :root {
    --ink: #0b0b0c;
    --ink-soft: #1c1c1f;
    --orange: #f7941d;
    --white: #ffffff;
    --grey: #d9d9d9;
    --line: #9a9a9a;
  }
  * { margin: 0; padding: 0; box-sizing: border-box; }
  html, body { width: 849px; height: 1200px; overflow: hidden; background: var(--ink); }
  .flyer {
    position: relative; width: 849px; height: 1200px; overflow: hidden;
    background: linear-gradient(180deg, #111113 0%, #19191b 45%, #0d0d0e 100%);
    font-family: "Montserrat", sans-serif; color: var(--white);
  }
  .hands-photo {
    position: absolute; left: 360px; top: 360px; width: 489px; height: 840px;
    background:
      radial-gradient(ellipse 55% 40% at 55% 72%, rgba(160,70,40,.75) 0%, rgba(70,30,20,.5) 45%, rgba(0,0,0,0) 75%),
      linear-gradient(115deg, rgba(0,0,0,0) 20%, rgba(200,200,200,.22) 38%, rgba(0,0,0,0) 55%),
      linear-gradient(180deg, #151517 0%, #2a2626 50%, #0e0c0c 100%);
  }
  .headline { position: absolute; top: 82px; left: 0; width: 100%; text-align: center; font-weight: 900; line-height: 1; text-transform: uppercase; }
  .headline .event-name { color: var(--orange); font-size: 86px; letter-spacing: 2px; }
  .headline .line { font-size: 66px; margin-top: 10px; letter-spacing: 1px; }
  .headline .accent { color: var(--orange); }
  .excerpt { position: absolute; top: 338px; right: 110px; font-style: italic; font-weight: 500; font-size: 30px; }
  .dates { position: absolute; top: 430px; left: 110px; font-family: "Oswald", sans-serif; font-weight: 600; line-height: 1.05; }
  .dates .label { font-size: 38px; }
  .dates .days { font-size: 44px; }
  .dates .year { font-family: "Montserrat", sans-serif; font-weight: 900; color: var(--orange); font-size: 96px; line-height: 1; }
  .venue { position: absolute; top: 432px; left: 450px; }
  .venue .time { font-family: "Oswald", sans-serif; font-weight: 600; font-size: 38px; line-height: 1.05; }
  .venue .address { font-size: 17px; font-weight: 500; line-height: 1.35; margin-top: 6px; color: var(--grey); }
  .themes {
    position: absolute; top: 650px; left: 110px; width: 630px; height: 118px;
    border: 2px solid var(--line); display: grid; grid-template-columns: 250px 1fr;
    padding: 20px 24px; row-gap: 18px; font-style: italic; font-weight: 500; font-size: 19px;
  }
  .themes li { list-style: none; display: flex; align-items: center; gap: 12px; white-space: nowrap; }
  .themes svg { width: 14px; height: 18px; flex: none; }
  .brand { position: absolute; top: 840px; left: 110px; display: flex; align-items: center; gap: 16px; }
  .brand .mark { width: 34px; height: 34px; border-radius: 50%; background: var(--orange); }
  .brand .name { font-size: 70px; font-weight: 500; letter-spacing: 3px; line-height: 1; }
  .brand-tagline { position: absolute; top: 918px; left: 110px; color: var(--orange); font-size: 18px; font-weight: 500; letter-spacing: 1px; text-transform: uppercase; }
  .contact-title { position: absolute; top: 990px; left: 110px; font-weight: 800; font-size: 38px; text-transform: uppercase; }
  .phone-pill { position: absolute; top: 1040px; left: 110px; width: 300px; height: 58px; border-radius: 29px; background: var(--orange); color: var(--ink); font-weight: 800; font-size: 36px; display: flex; align-items: center; justify-content: center; }
  .contact-line { position: absolute; left: 110px; display: flex; align-items: center; gap: 14px; font-size: 20px; font-weight: 500; }
  .contact-line svg { width: 20px; height: 16px; }
  .email { top: 1118px; }
  .web { top: 1152px; }
</style>
</head>
<body>
<div class="flyer">
  <div class="hands-photo" role="img" aria-label="Photo of hands folded in prayer under a soft beam of light"></div>

  <h1 class="headline">
    <div class="event-name">Selvin</div>
    <div class="line">A Friday Night</div>
    <div class="line">In the <span class="accent">Prophetic</span></div>
  </h1>
  <p class="excerpt">...And they prophesied also</p>

  <div class="dates">
    <div class="label">2 FRIDAY NIGHT</div>
    <div class="days">10/25 &amp; 11/29</div>
    <div class="year">2019</div>
  </div>

  <div class="venue">
    <div class="time">6:30PM-9:00PM</div>
    <p class="address">Hollard Community Center<br>(Downtown Portland) 482<br>Wendle Street Portland,<br>ME 04102</p>
  </div>

  <ul class="themes">
    <li><svg viewBox="0 0 14 18"><path d="M2 1 L12 9 L2 17" fill="none" stroke="#f7941d" stroke-width="4"/></svg>Prophetic</li>
    <li><svg viewBox="0 0 14 18"><path d="M2 1 L12 9 L2 17" fill="none" stroke="#f7941d" stroke-width="4"/></svg>Climbing in the Spirit</li>
    <li><svg viewBox="0 0 14 18"><path d="M2 1 L12 9 L2 17" fill="none" stroke="#f7941d" stroke-width="4"/></svg>Healing</li>
    <li><svg viewBox="0 0 14 18"><path d="M2 1 L12 9 L2 17" fill="none" stroke="#f7941d" stroke-width="4"/></svg>Higher level of Anointing...</li>
  </ul>

  <div class="brand">
    <span class="mark"></span>
    <span class="name">TOVIK</span>
  </div>
  <p class="brand-tagline">A Voice to All Nations</p>

  <h2 class="contact-title">Contact Us</h2>
  <div class="phone-pill">207-555-3841</div>
  <p class="contact-line email"><svg viewBox="0 0 20 16"><rect width="20" height="16" rx="2" fill="#f7941d"/><path d="M1 2 L10 9 L19 2" fill="none" stroke="#111" stroke-width="2"/></svg>contact@brimfield-hall.org</p>
  <p class="contact-line web"><svg viewBox="0 0 20 16"><rect width="20" height="16" rx="2" fill="#f7941d"/><rect x="2" y="4" width="16" height="10" fill="#111"/></svg>www.tovik.org</p>
</div>
</body>
</html>
```